Powerpoint design for management consultant

We need a powerpoint design to use for our corporate presentations, proposal summaries and for delivering report recommendations.

Target Market(s)

Executives in Government & Private Industry

Industry/Entity Type

Consultant

Requirements
Must have
• Must use the company logo contained in the uploaded files.
Must be a powerpoint template file (.potx) that can be used with Powerpoint 2007 and later.
Must have a title slide.
Must have a purpose slide (in today's presentation we will cover ....)
Must have an agenda slide.
Must have three topic slides (topic1, topic2, topic3) as transition slides
Must support side by side comparisons
Any images used must be available royalty/ license free
Must have a summary slide.
Must have a questions slide at the end.
Must have a footer containing slide number in format of x of y.
Must have a footer containing presentation name.
Must have a footer containing the presentation date.
Must have a footer containing "confidential"
Nice to have
• The powerpoint should support the ability to represent data using infographics.
Should not have
• no tag lines or references to being management consultants. must not use custom fonts.

```html
<!DOCTYPE html>
<html lang="en">
<head>
<meta charset="utf-8">
<title>Summary slide</title>
<link href="https://fonts.googleapis.com/css2?family=Ubuntu:wght@300;400;700&display=swap" rel="stylesheet">
<style>
  :root {
    --paper: #f1f0ee;
    --paper-shade: #e6e5e2;
    --edge: #3a3a3a;
    --band: #efb07f;
    --ink: #1f1f1f;
    --muted: #6b6b6b;
    --brand: #2a3a4e;
  }
  html, body {
    margin: 0;
    padding: 0;
    width: 1200px;
    height: 898px;
    overflow: hidden;
  }
  .slide {
    position: relative;
    width: 1200px;
    height: 898px;
    background: radial-gradient(ellipse at 30% 40%, #f7f6f4 0%, var(--paper) 55%, var(--paper-shade) 100%);
    font-family: "Ubuntu", Arial, sans-serif;
    color: var(--ink);
    overflow: hidden;
    border-left: 2px solid var(--edge);
    box-sizing: border-box;
  }
  .title-band {
    position: absolute;
    left: 460px;
    top: 239px;
    width: 740px;
    height: 80px;
    background: var(--band);
  }
  .title-band h1 {
    margin: 0;
    position: absolute;
    left: 74px;
    top: 12px;
    font-weight: 300;
    font-size: 38px;
    line-height: 1.3;
    color: var(--ink);
  }
  .summary-text {
    position: absolute;
    left: 104px;
    top: 368px;
    width: 1044px;
    margin: 0;
    font-weight: 300;
    font-size: 24px;
    line-height: 35.5px;
    text-align: justify;
  }
  .summary-text sup {
    font-size: 14px;
    line-height: 0;
  }
  .footer-meta {
    position: absolute;
    top: 862px;
    font-size: 20px;
    font-weight: 300;
    color: var(--muted);
  }
  .footer-date { left: 12px; }
  .footer-confidential { left: 170px; }
  .footer-name { left: 373px; }
  .brand-name {
    position: absolute;
    left: 810px;
    top: 836px;
    font-size: 56px;
    font-weight: 700;
    letter-spacing: 1px;
    color: var(--brand);
    line-height: 1;
  }
  .page-number {
    position: absolute;
    left: 1154px;
    top: 856px;
    font-size: 26px;
    font-weight: 400;
    color: var(--brand);
  }
</style>
</head>
<body>
  <main class="slide">
    <div class="title-band">
      <h1>summary</h1>
    </div>

    <p class="summary-text">In todays presentation we will cover “Structural Aluminium”. In engineering parlance the term aluminium (or aluminum) covers any aluminium-based material, and embraces the alloys as well as the pure metal. With an annual consumption of 35 million metric tons<sup>[9]</sup>, aluminium is one of the most commonly used metals globally. Its lightness coupled with its strength, conductivity, barrier properties and its excellent corrosion resistance have all been and continue to be its most important advantages and the main reasons for the continued growth in the usage of aluminium.</p>

    <footer>
      <span class="footer-meta footer-date">23-Oct-13</span>
      <span class="footer-meta footer-confidential">Confidential</span>
      <span class="footer-meta footer-name">Presentation name</span>
      <span class="brand-name">KORVANT</span>
      <span class="page-number">15</span>
    </footer>
  </main>
</body>
</html>
```